Dean Hollis Business Card

In addition to my name design (file uploaded), black print on white card stock, e-mail address should be presented as a typical e-mail address, i.e., underlined and in blue ink, the card should include the following information:
Professor of Aviation Technology
Accident Litigation Expert Witness
Master Certificated Flight Instructor

dhollis@vexmail.example
Anchorage, Alaska
(907) 318-5074

```html
<!DOCTYPE html>
<html lang="en">
<head>
<meta charset="utf-8">
<title>Dean Hollis Business Card</title>
<link rel="stylesheet" href="https://fonts.googleapis.com/css2?family=Lato:wght@400;700;900&display=swap">
<style>
  :root {
    --backdrop: #2a2a2a;
    --card: #ffffff;
    --ink: #151515;
    --ink-soft: #2b2b2b;
    --rule: #3a3a3a;
    --link: #1f8fd1;
  }
  * { margin: 0; padding: 0; box-sizing: border-box; }
  html, body {
    width: 1200px;
    height: 900px;
    overflow: hidden;
    background: var(--backdrop);
    font-family: "Lato", Arial, sans-serif;
  }
  .sheet {
    width: 1200px;
    height: 900px;
    display: flex;
    flex-direction: column;
    align-items: center;
    justify-content: center;
    gap: 36px;
  }
  .card {
    width: 700px;
    height: 400px;
    background: var(--card);
    color: var(--ink);
    display: flex;
    flex-direction: column;
    align-items: center;
  }
  .wordmark {
    font-weight: 900;
    font-size: 62px;
    letter-spacing: 1px;
    text-transform: uppercase;
    color: var(--ink);
    line-height: 1;
  }
  .card--back { justify-content: center; }
  .card--front { padding-top: 78px; }
  .details {
    margin-top: 56px;
    text-align: center;
    color: var(--ink-soft);
  }
  .details__name {
    font-weight: 700;
    font-size: 20px;
    color: var(--ink);
    margin-bottom: 2px;
  }
  .details__title {
    font-size: 17px;
    line-height: 1.3;
  }
  .details__rule {
    width: 430px;
    height: 1px;
    background: var(--rule);
    margin: 12px auto 10px;
  }
  .details__contact { font-size: 17px; }
  .details__email {
    color: var(--link);
    text-decoration: underline;
  }
</style>
</head>
<body>
  <main class="sheet">
    <section class="card card--back" aria-label="Card back">
      <div class="wordmark">Dean E. Hollis</div>
    </section>
    <section class="card card--front" aria-label="Card front">
      <div class="wordmark">Dean E. Hollis</div>
      <div class="details">
        <p class="details__name">Dean E. Hollis</p>
        <p class="details__title">Professor of Aviation Technology</p>
        <p class="details__title">Accident Litigation Expert Witness</p>
        <p class="details__title">Master Certificated Flight Instructor</p>
        <div class="details__rule"></div>
        <p class="details__contact">Anchorage, Alaska | (907) 318-5074 | <span class="details__email">dhollis@vexmail.example</span></p>
      </div>
    </section>
  </main>
</body>
</html>
```